Vital Spark Electrical in need of a business card design

We need a new business card designed for our electrical business. We have a logo already which I will attach below.
Would like the business card to be..
-BLACK background preferably, possibly white back ground behind logo if colours clash.
-White & Blue (logo blue) text
Something that makes the logo pop, & a modern look. Possibly minimal clean format.

REQUIRE:
-Logo on front & back

TEXT TO INCLUDE (ON ONE SIDE):

Tom Harlow
Director/Electrician
M: 0417 365 208
E:info@vitalsparkelectrical-example.com.au
W:www.vitalsparkelectrical-example.com.au
R.E.C 57318

Custom/New Homes
Renovations
Commercial Office/Shop Fit-outs
Communications & Security Cameras
Electric Vehicle Chargers
Airconditioning
Updates

Requirements
Nice to have
• Possibly even lighten the grey shades for the words 'Vital' & 'Spark' to be more easily read on a black background.

```html
<!DOCTYPE html>
<html lang="en">
<head>
<meta charset="utf-8">
<title>Vital Spark Electrical – Business Card</title>
<link href="https://fonts.googleapis.com/css2?family=Open+Sans:wght@400;600&family=Oswald:wght@400&display=swap" rel="stylesheet">
<style>
  :root {
    --page: #ffffff;
    --card-light: #f4f5f6;
    --card-light-edge: #e3e5e7;
    --slate: #2e3a45;
    --slate-text: #2a343d;
    --muted: #4b5560;
    --blue: #0a9ad6;
    --blue-deep: #1f6fb2;
    --black: #000000;
    --white: #ffffff;
    --light-grey: #d9dcdf;
  }
  html, body {
    margin: 0;
    width: 1200px;
    height: 1000px;
    overflow: hidden;
    background: var(--page);
  }
  .canvas {
    position: relative;
    width: 1200px;
    height: 1000px;
  }
  .card {
    position: absolute;
    box-shadow: 8px 10px 14px rgba(0, 0, 0, 0.18);
    font-family: "Open Sans", sans-serif;
  }
  /* Front */
  .card-front {
    left: 275px;
    top: 52px;
    width: 675px;
    height: 385px;
    background: radial-gradient(ellipse at 30% 20%, var(--white) 0%, var(--card-light) 60%, var(--card-light-edge) 100%);
    overflow: hidden;
  }
  .brand-name {
    position: absolute;
    left: 30px;
    top: 44px;
    margin: 0;
    font-family: "Open Sans", sans-serif;
    font-weight: 600;
    font-size: 44px;
    line-height: 1;
    color: var(--slate-text);
    letter-spacing: -0.5px;
    white-space: nowrap;
  }
  .person {
    position: absolute;
    right: 53px;
    top: 174px;
    text-align: right;
  }
  .person-name {
    margin: 0;
    font-family: "Oswald", sans-serif;
    font-size: 29px;
    line-height: 36px;
    color: var(--slate-text);
  }
  .person-role {
    margin: 0;
    font-size: 15px;
    line-height: 22px;
    color: var(--muted);
  }
  .person-licence {
    margin: 0;
    font-size: 15px;
    line-height: 22px;
    color: var(--blue-deep);
  }
  .name-marker {
    position: absolute;
    right: 0;
    top: 190px;
    width: 38px;
    height: 45px;
    background: var(--blue);
  }
  .contact-list {
    position: absolute;
    left: 34px;
    top: 278px;
    margin: 0;
    padding: 0;
    list-style: none;
  }
  .contact-item {
    display: flex;
    align-items: center;
    height: 25.5px;
    font-size: 17px;
    color: var(--slate-text);
  }
  .contact-icon {
    width: 18px;
    height: 18px;
    margin-right: 9px;
    flex: none;
  }
  .base-band {
    position: absolute;
    left: 0;
    bottom: 0;
    width: 100%;
    height: 24px;
    background: var(--slate);
  }
  /* Back */
  .card-back {
    left: 273px;
    top: 521px;
    width: 677px;
    height: 386px;
    background: var(--black);
  }
  .brand-name-back {
    position: absolute;
    left: 0;
    right: 0;
    top: 150px;
    margin: 0;
    text-align: center;
    font-weight: 600;
    font-size: 44px;
    line-height: 1;
    color: var(--light-grey);
    letter-spacing: -0.5px;
  }
  .services {
    position: absolute;
    left: 0;
    right: 0;
    top: 312px;
    margin: 0;
    padding: 0;
    list-style: none;
    font-size: 15px;
    color: var(--white);
  }
  .service {
    position: absolute;
    white-space: nowrap;
  }
</style>
</head>
<body>
<main class="canvas">
  <section class="card card-front" aria-label="Card front">
    <h1 class="brand-name">Vital Spark Electrical</h1>

    <div class="person">
      <p class="person-name">Tom Harlow</p>
      <p class="person-role">Director/Electrician</p>
      <p class="person-licence">R.E.C 57318</p>
    </div>
    <div class="name-marker"></div>

    <ul class="contact-list">
      <li class="contact-item">
        <svg class="contact-icon" viewBox="0 0 18 18" aria-hidden="true">
          <rect x="4" y="0.8" width="10" height="16.4" rx="2" fill="none" stroke="#0a9ad6" stroke-width="1.6"/>
          <circle cx="9" cy="14.5" r="0.9" fill="#0a9ad6"/>
        </svg>
        0417 365 208
      </li>
      <li class="contact-item">
        <svg class="contact-icon" viewBox="0 0 18 18" aria-hidden="true">
          <rect x="1" y="4" width="16" height="11" fill="none" stroke="#0a9ad6" stroke-width="1.5"/>
          <path d="M1 4 L9 10.5 L17 4 M1 15 L7 9 M17 15 L11 9" fill="none" stroke="#0a9ad6" stroke-width="1.3"/>
        </svg>
        info@vitalsparkelectrical-example.com.au
      </li>
      <li class="contact-item">
        <svg class="contact-icon" viewBox="0 0 18 18" aria-hidden="true">
          <circle cx="9" cy="9" r="7.5" fill="none" stroke="#0a9ad6" stroke-width="1.4"/>
          <ellipse cx="9" cy="9" rx="3.3" ry="7.5" fill="none" stroke="#0a9ad6" stroke-width="1.2"/>
          <path d="M1.5 9 H16.5 M3 5 H15 M3 13 H15" stroke="#0a9ad6" stroke-width="1.1"/>
        </svg>
        www.vitalsparkelectrical-example.com.au
      </li>
    </ul>

    <div class="base-band"></div>
  </section>

  <section class="card card-back" aria-label="Card back">
    <h2 class="brand-name-back">Vital Spark Electrical</h2>
    <ul class="services">
      <li class="service" style="left:55px; top:0;">Custom/New Homes</li>
      <li class="service" style="left:255px; top:2px;">Renovations</li>
      <li class="service" style="left:379px; top:2px;">Commercial Office/Shop Fit-outs</li>
      <li class="service" style="left:36px; top:30px;">Communications &amp; Security Cameras</li>
      <li class="service" style="left:315px; top:30px;">Electric Vehicle Chargers</li>
      <li class="service" style="left:514px; top:30px;">Airconditioning</li>
    </ul>
  </section>
</main>
</body>
</html>
```